PIKEmoor box Graphic design on existing box dye cut.

we are a flooring company and we are making a sample box. the logo and information that need to be on the box is already established. we just need someone to lay it out on the box "DYE_CUT" . PLEASE CHANGE DASHES ON LOOK TOUCH PICK TO DOTS AND REMOVE THE EXCLAMATION POINT ALSO, please give me a lighter version of the logo...it appears a bit dark on the box. perhaps lighten a bit. .so we need to work with someone who understands how to work with a box dye cut. We want to wrap the logo around the entire 4 sides of the box and leave the top and bottom a black color. The inside of the box will have a similar photo with bullet points (be creative how to include them). I have enclosed a picture of this how it should read. Also, the large inside flap will have a specification sheet. I have included photos of this sheet for your reference… all spec information needs to be included as written. We need to include a QR code on this inside flap which will later allow architects to download the spec.The very front cover that we submitted with the PIKEMOOR look touch pick…I would like a few reeditions of the font on this as I am not completely sold on the font. I am including pictures of how it should look, from a cut and paste model I made.

Target Market(s)

architects and designers

Industry/Entity Type

Architecture

Colors
474747

Requirements
Must have
• Graphic designer MUST know how to work with dye cuts provided and scale artwork to work on dye cut sizes provided. must look professional and elegant this is for architects and designers
Nice to have
• box must look good from all sides . short and long sides. pikemoor photo needs to be on all 4 sides...

```html
<!DOCTYPE html>
<html lang="en">
<head>
<meta charset="utf-8">
<title>PIKEmoor Sample Box – Die Cut Layout</title>
<link rel="stylesheet" href="https://fonts.googleapis.com/css2?family=Arimo:ital,wght@0,400;0,700;1,700&family=Lato:wght@300;700&family=Great+Vibes&display=swap">
<style>
  :root{
    --ink:#000000;
    --fold:#e3000f;
    --dim:#1414ff;
    --board:#ffffff;
    --charcoal:#474747;
    --brand:#2a2a2a;
    --wood-light:#d4d4d4;
    --wood-mid:#9a9a9a;
    --wood-dark:#5e5e5e;
    --script:#f4f4f4;
    --sheet-text:#2b2b2b;
  }
  html,body{margin:0;padding:0;width:1200px;height:893px;overflow:hidden;background:var(--board);}
  .dieline{display:block;width:1200px;height:893px;}
  .cut{fill:var(--board);stroke:var(--ink);stroke-width:1.4;}
  .fold{fill:none;stroke:var(--fold);stroke-width:1.4;}
  .base{fill:var(--ink);}
  .dim-line{stroke:var(--dim);stroke-width:1;fill:none;}
  .dim-label{fill:var(--dim);font-family:"Arimo",Arial,sans-serif;font-size:30px;}
  .dim-label .frac{font-size:19px;}
  .dim-total{fill:var(--dim);font-family:"Arimo",Arial,sans-serif;font-weight:700;font-style:italic;font-size:36px;}
  .dim-total .frac{font-size:22px;}
  .brand{font-family:"Lato",Arial,sans-serif;font-weight:700;font-size:30px;fill:var(--brand);letter-spacing:1px;}
  .motto{font-family:"Lato",Arial,sans-serif;font-weight:300;font-size:11.5px;fill:var(--brand);letter-spacing:2px;}
  .script{font-family:"Great Vibes",cursive;font-size:13px;fill:var(--script);}
  .bullet-bar{fill:var(--charcoal);}
  .bullet-text{font-family:"Arimo",Arial,sans-serif;font-size:6px;fill:#ffffff;}
  .bullet-head{font-family:"Arimo",Arial,sans-serif;font-size:6.5px;font-weight:700;fill:#ffffff;}
  .spec-label{font-family:"Arimo",Arial,sans-serif;font-size:4.6px;font-weight:700;fill:var(--sheet-text);}
  .spec-value{font-family:"Arimo",Arial,sans-serif;font-size:4.6px;fill:var(--sheet-text);}
  .spec-title{font-family:"Arimo",Arial,sans-serif;font-size:5.4px;font-weight:700;fill:var(--sheet-text);}
  .spec-rule{stroke:var(--sheet-text);stroke-width:1.6;}
  .drawing-slot{fill:#ececec;stroke:#b5b5b5;stroke-width:.6;}
</style>
</head>
<body>
<svg class="dieline" viewBox="0 0 1500 1116.25" xmlns="http://www.w3.org/2000/svg">
  <defs>
    <linearGradient id="woodTone" x1="0" y1="0" x2="1" y2="1">
      <stop offset="0" stop-color="#9a9a9a"/>
      <stop offset=".45" stop-color="#d4d4d4"/>
      <stop offset="1" stop-color="#5e5e5e"/>
    </linearGradient>
    <marker id="arrow" viewBox="0 0 10 10" refX="10" refY="5" markerWidth="9" markerHeight="9" orient="auto-start-reverse">
      <path d="M0,1 L10,5 L0,9" fill="none" stroke="#1414ff" stroke-width="1.2"/>
    </marker>
  </defs>

  <g class="flaps">
    <path class="cut" d="M510,304 V150 H598 V145 H660 V150 H820 V304 Z"/>
    <path class="cut" d="M510,897 V1052 H598 V1057 H662 V1052 H820 V897 Z"/>
    <rect class="cut" x="353" y="323" width="154" height="157"/>
    <rect class="cut" x="822" y="323" width="154" height="154"/>
    <rect class="cut" x="353" y="720" width="154" height="157"/>
    <rect class="cut" x="822" y="725" width="154" height="152"/>
    <path class="cut" d="M350,485 H200 V578 H172 Q168,578 168,585 V615 Q168,622 172,622 H200 V715 H350 Z"/>
    <line class="fold" x1="200" y1="578" x2="200" y2="622"/>
    <path class="cut" d="M1305,477 L1300,360 C1300,322 1390,318 1430,368 C1452,396 1457,430 1457,477 Z"/>
    <path class="cut" d="M1300,725 L1305,830 C1310,872 1405,872 1435,815 C1452,785 1457,760 1457,725 Z"/>
  </g>

  <rect class="base" x="507" y="472" width="315" height="255"/>

  <g class="wall wall-top" transform="translate(507,304)">
    <rect width="315" height="168" fill="url(#woodTone)" role="img" aria-label="Grey weathered wood planks with a dog peeking through a hole"/>
    <text class="brand" x="83" y="44">PIKEMOOR</text>
    <text class="motto" x="84" y="60">LOOK · TOUCH · PICK</text>
    <text class="script" x="148" y="155">Crafted for Considered Spaces</text>
  </g>

  <g class="wall wall-bottom" transform="translate(822,897) rotate(180)">
    <rect width="315" height="170" fill="url(#woodTone)" role="img" aria-label="Grey weathered wood planks with a dog peeking through a hole"/>
    <text class="brand" x="83" y="44">PIKEMOOR</text>
    <text class="motto" x="84" y="60">LOOK · TOUCH · PICK</text>
    <text class="script" x="148" y="155">Crafted for Considered Spaces</text>
  </g>

  <g class="wall wall-left" transform="translate(350,720) rotate(-90)">
    <rect width="240" height="157" fill="url(#woodTone)" role="img" aria-label="Grey weathered wood planks with a dog peeking through a hole"/>
    <text class="brand" x="30" y="33">PIKEMOOR</text>
    <text class="motto" x="31" y="48">LOOK · TOUCH · PICK</text>
    <text class="script" x="95" y="146">Crafted for Considered Spaces</text>
  </g>

  <g class="wall wall-right" transform="translate(983,477) rotate(90)">
    <rect width="248" height="161" fill="url(#woodTone)" role="img" aria-label="Grey weathered wood planks with a dog peeking through a hole"/>
    <text class="brand" x="40" y="36">PIKEMOOR</text>
    <text class="motto" x="41" y="52">LOOK · TOUCH · PICK</text>
    <text class="script" x="100" y="150">Crafted for Considered Spaces</text>
  </g>

  <path class="cut" d="M983,470 H1300 V730 H990 L983,722 Z"/>
  <g class="spec-sheet" transform="translate(1290,480) rotate(90)">
    <line class="spec-rule" x1="10" y1="7" x2="235" y2="7"/>
    <g class="spec-rows">
      <text class="spec-label" x="12" y="20">Species:</text><text class="spec-value" x="80" y="20">Blanched French White Oak</text>
      <text class="spec-label" x="12" y="31">Construction:</text><text class="spec-value" x="80" y="31">Engineered hardwood</text>
      <text class="spec-label" x="12" y="42">Plank Sizes:</text><text class="spec-value" x="80" y="42">5" and 7" wide, random lengths</text>
      <text class="spec-label" x="12" y="53">Pattern Available:</text><text class="spec-value" x="80" y="53">Herringbone and chevron</text>
      <text class="spec-label" x="12" y="64">Grade:</text><text class="spec-value" x="80" y="64">Select, rustic and character</text>
      <text class="spec-label" x="12" y="75">Texture:</text><text class="spec-value" x="80" y="75">Wire brushed</text>
      <text class="spec-label" x="12" y="86">Finish:</text><text class="spec-value" x="80" y="86">UV oil</text>
      <text class="spec-label" x="12" y="97">Wear Layer:</text><text class="spec-value" x="80" y="97">3mm sawn face</text>
      <text class="spec-label" x="12" y="108">UV Finishing:</text><text class="spec-value" x="80" y="108">Low VOC matte</text>
      <text class="spec-label" x="12" y="119">Certifications:</text><text class="spec-value" x="80" y="119">FSC and CARB2 compliant</text>
      <text class="spec-label" x="12" y="130">Structural:</text><text class="spec-value" x="80" y="130">Tongue and groove</text>
      <text class="spec-label" x="12" y="141">Installation:</text><text class="spec-value" x="80" y="141">Float, glue or nail</text>
      <text class="spec-value" x="12" y="158">Matching stair nosing and trims available.</text>
      <text class="spec-value" x="12" y="166">Verify site conditions before install.</text>
      <text class="spec-value" x="12" y="174">Request samples from your rep.</text>
    </g>
    <text class="spec-title" x="12" y="194">FABRICATED SQUARE EDGE STAIR NOSE, TREADS &amp; TRANSITIONS</text>
    <text class="spec-title" x="60" y="202">THAT MATCH YOUR WOOD FLOOR</text>
    <rect class="drawing-slot" x="12" y="218" width="130" height="62" role="img" aria-label="Technical profile drawing of a square edge stair nose"/>
    <rect class="drawing-slot" x="160" y="240" width="60" height="40" role="img" aria-label="Technical profile drawing of a flush transition"/>
  </g>

  <g class="wall wall-feature" transform="translate(1457,477) rotate(90)">
    <rect width="248" height="157" fill="url(#woodTone)" role="img" aria-label="Grey weathered wood planks with a dog peeking through a hole"/>
    <text class="brand" x="40" y="34">PIKEMOOR</text>
    <text class="motto" x="41" y="50">LOOK · TOUCH · PICK</text>
    <g class="bullets">
      <rect class="bullet-bar" x="112" y="58" width="136" height="11"/>
      <text class="bullet-head" x="116" y="66">Ultimate design flexibility with:</text>
      <rect class="bullet-bar" x="124" y="72" width="124" height="10"/>
      <text class="bullet-text" x="128" y="79">• Multiple widths and patterns</text>
      <rect class="bullet-bar" x="136" y="85" width="112" height="10"/>
      <text class="bullet-text" x="140" y="92">• Wide plank options</text>
      <rect class="bullet-bar" x="148" y="98" width="100" height="10"/>
      <text class="bullet-text" x="152" y="105">• Long lengths for open rooms</text>
      <rect class="bullet-bar" x="160" y="111" width="88" height="10"/>
      <text class="bullet-text" x="164" y="118">• Made for commercial spaces</text>
    </g>
    <text class="script" x="12" y="145">Crafted for Considered Spaces</text>
  </g>

  <g class="folds">
    <rect class="fold" x="507" y="304" width="315" height="593"/>
    <rect class="fold" x="350" y="480" width="157" height="240"/>
    <rect class="fold" x="822" y="477" width="161" height="248"/>
    <rect class="fold" x="1300" y="477" width="157" height="248"/>
  </g>

  <g class="dimensions">
    <line class="dim-line" x1="168" y1="70" x2="1457" y2="70" marker-start="url(#arrow)" marker-end="url(#arrow)"/>
    <line class="dim-line" x1="168" y1="60" x2="168" y2="590"/>
    <line class="dim-line" x1="1457" y1="60" x2="1457" y2="420"/>
    <text class="dim-total" x="766" y="86">42<tspan class="frac" dx="4" dy="-10">3</tspan><tspan class="frac">/</tspan><tspan class="frac" dy="10">16</tspan></text>

    <line class="dim-line" x1="58" y1="143" x2="58" y2="1057" marker-start="url(#arrow)" marker-end="url(#arrow)"/>
    <line class="dim-line" x1="48" y1="143" x2="600" y2="143"/>
    <line class="dim-line" x1="48" y1="1057" x2="600" y2="1057"/>
    <text class="dim-total" x="22" y="614">29<tspan class="frac" dx="4" dy="-10">7</tspan><tspan class="frac">/</tspan><tspan class="frac" dy="10">8</tspan></text>

    <line class="dim-line" x1="750" y1="152" x2="750" y2="302" marker-start="url(#arrow)" marker-end="url(#arrow)"/>
    <line class="dim-line" x1="750" y1="899" x2="750" y2="1053" marker-start="url(#arrow)" marker-end="url(#arrow)"/>
    <line class="dim-line" x1="750" y1="487" x2="750" y2="715"/>
    <line class="dim-line" x1="728" y1="487" x2="772" y2="487"/>
    <line class="dim-line" x1="728" y1="715" x2="772" y2="715"/>
    <line class="dim-line" x1="200" y1="522" x2="1457" y2="522"/>
    <line class="dim-line" x1="200" y1="522" x2="350" y2="522" marker-start="url(#arrow)" marker-end="url(#arrow)"/>
    <line class="dim-line" x1="510" y1="522" x2="820" y2="522" marker-start="url(#arrow)" marker-end="url(#arrow)"/>
    <line class="dim-line" x1="985" y1="522" x2="1298" y2="522" marker-start="url(#arrow)" marker-end="url(#arrow)"/>

    <text class="dim-label" x="722" y="240">5<tspan class="frac" dy="-12">1</tspan><tspan class="frac">/</tspan><tspan class="frac" dy="12">16</tspan></text>
    <text class="dim-label" x="726" y="408">5<tspan class="frac" dy="-12">1</tspan><tspan class="frac">/</tspan><tspan class="frac" dy="12">8</tspan></text>
    <text class="dim-label" x="252" y="532">4<tspan class="frac" dy="-12">7</tspan><tspan class="frac">/</tspan><tspan class="frac" dy="12">8</tspan></text>
    <text class="dim-label" x="398" y="535">4<tspan class="frac" dy="-12">15</tspan><tspan class="frac">/</tspan><tspan class="frac" dy="12">16</tspan></text>
    <text class="dim-label" x="634" y="535">9<tspan class="frac" dy="-12">15</tspan><tspan class="frac">/</tspan><tspan class="frac" dy="12">16</tspan></text>
    <text class="dim-label" x="728" y="612">7<tspan class="frac" dy="-12">1</tspan><tspan class="frac">/</tspan><tspan class="frac" dy="12">2</tspan></text>
    <text class="dim-label" x="880" y="535">5<tspan class="frac" dy="-12">1</tspan><tspan class="frac">/</tspan><tspan class="frac" dy="12">4</tspan></text>
    <text class="dim-label" x="1110" y="535">10<tspan class="frac" dy="-12">3</tspan><tspan class="frac">/</tspan><tspan class="frac" dy="12">8</tspan></text>
    <text class="dim-label" x="1350" y="535">5<tspan class="frac" dy="-12">3</tspan><tspan class="frac">/</tspan><tspan class="frac" dy="12">16</tspan></text>
    <text class="dim-label" x="726" y="818">5<tspan class="frac" dy="-12">1</tspan><tspan class="frac">/</tspan><tspan class="frac" dy="12">8</tspan></text>
    <text class="dim-label" x="722" y="986">5<tspan class="frac" dy="-12">1</tspan><tspan class="frac">/</tspan><tspan class="frac" dy="12">16</tspan></text>
  </g>
</svg>
</body>
</html>
```